Harbor Loom Flooring Letterhead

Letterhead used for business reasons. It must be editable and easy to use.

Address is 5127 W. Pelican Lane Port Sorrel FL 34291 - 941.538.2194

```html
<!DOCTYPE html>
<html lang="en">
<head>
<meta charset="utf-8">
<title>Harbor Loom Flooring Letterhead</title>
<link href="https://fonts.googleapis.com/css2?family=Montserrat:wght@400;500;600&display=swap" rel="stylesheet">
<style>
  :root {
    --backdrop: #e9e9ea;
    --paper: #ffffff;
    --ink: #3a3a3a;
    --ink-soft: #5a5a5a;
    --brand-orange: #e08b24;
    --brand-grey: #9b918c;
    --signature-tone: #ececec;
  }
  * { box-sizing: border-box; margin: 0; padding: 0; }
  html, body {
    width: 1200px; height: 908px; overflow: hidden;
    background: var(--backdrop);
    font-family: "Montserrat", Arial, sans-serif;
    color: var(--ink);
  }
  .letterhead {
    position: absolute; left: 295px; top: 23px;
    width: 610px; height: 862px;
    background: var(--paper);
    box-shadow: 0 2px 10px rgba(0,0,0,0.12);
    overflow: hidden;
  }
  .brand-name {
    position: absolute; left: 58px; top: 74px;
    font-size: 21px; font-weight: 500; letter-spacing: 0.3px;
    color: var(--brand-orange);
  }
  .contact-block {
    position: absolute; left: 372px; top: 56px;
    font-size: 8.5px; line-height: 1.55; color: var(--ink-soft);
    font-style: normal;
  }
  .contact-row { display: flex; align-items: center; gap: 5px; padding-left: 12px; }
  .contact-row svg { width: 8px; height: 8px; flex: none; }
  .recipient {
    position: absolute; left: 58px; top: 168px;
    font-size: 9px; line-height: 1.5; color: var(--ink-soft);
  }
  .recipient-name { font-weight: 600; color: var(--ink); }
  .letter-body {
    position: absolute; left: 90px; top: 250px; width: 440px;
    font-size: 9px; line-height: 1.65; color: var(--ink-soft);
  }
  .letter-body p + p { margin-top: 14px; }
  .sign-off {
    position: absolute; left: 150px; top: 520px;
    font-size: 9px; line-height: 1.5; color: var(--ink-soft);
  }
  .signature-area {
    width: 120px; height: 30px; margin: 4px 0 4px 20px;
    background: var(--signature-tone); border-radius: 3px;
  }
  .signer-name { font-weight: 600; color: var(--ink); }
  .footer-band { position: absolute; left: 0; bottom: 0; width: 610px; height: 12px; }
</style>
</head>
<body>
  <main class="letterhead">
    <div class="brand-name">Harbor Loom Flooring</div>

    <address class="contact-block">
      <div>5127 W. Pelican Lane</div>
      <div>Port Sorrel FL 34291</div>
      <div class="contact-row">
        <svg viewBox="0 0 10 10"><circle cx="5" cy="5" r="5" fill="var(--brand-orange)"/><path d="M3 2.5l1.2 0 .5 1.5-.8.6a4 4 0 0 0 1.5 1.5l.6-.8 1.5.5v1.2c-2.6.2-4.7-1.9-4.5-4.5z" fill="#fff"/></svg>
        <span>941.538.2194</span>
      </div>
      <div class="contact-row">
        <svg viewBox="0 0 10 10"><circle cx="5" cy="5" r="5" fill="var(--brand-orange)"/><rect x="2.3" y="3.2" width="5.4" height="3.6" fill="#fff"/><path d="M2.3 3.2L5 5.2 7.7 3.2" fill="none" stroke="var(--brand-orange)" stroke-width=".6"/></svg>
        <span>office@harborloomflooring.net</span>
      </div>
      <div class="contact-row">
        <svg viewBox="0 0 10 10"><circle cx="5" cy="5" r="5" fill="var(--brand-orange)"/><circle cx="5" cy="5" r="2.6" fill="none" stroke="#fff" stroke-width=".7"/><path d="M2.4 5h5.2M5 2.4c-1.2 1.5-1.2 3.7 0 5.2M5 2.4c1.2 1.5 1.2 3.7 0 5.2" fill="none" stroke="#fff" stroke-width=".6"/></svg>
        <span>www.harborloomflooring.com</span>
      </div>
    </address>

    <section class="recipient">
      <div class="recipient-name">Renata Coleman</div>
      <div>Director</div>
      <div>City, State, Zip Code</div>
    </section>

    <section class="letter-body">
      <p>Proin gravida nibh vel velit auctor aliquet. Aenean sollicitudin, lorem quis bibendum auctor, nisi elit consequat ipsum, nec sagittis sem nibh id elit. Duis sed odio sit amet nibh vulputate cursus a sit amet mauris. Morbi accumsan ipsum velit. Nam nec tellus a odio tincidunt auctor a ornare odio. Sed non mauris vitae erat consequat auctor eu in elit. Class aptent taciti sociosqu ad litora torquent per conubia nostra, per inceptos himenaeos. Mauris in erat justo. Nullam ac urna eu felis dapibus</p>
      <p>This is a placeholder version of Lorem Ipsum. Proin gravida nibh vel velit auctor aliquet. Aenean sollicitudin, lorem quis bibendum auctor, nisi elit consequat ipsum, lit. Duis sed odio sit amet nibh vulputate cursus a sit amet mauris. Morbi</p>
      <p>Nullam ac urna eu felis dapibus condimentum sit amet a augue. Sed non neque elit. Sed ut imperdiet nisi. Proin condimentum fermentum nunc. Etiam pharetra, erat sed fermentum feugiat, velit mauris egestas quam.Nullam ac urna eu felis dapibus condimentum sit amet a augue. Sed non neque elit. Sed ut imperdiet nisi. Proin condimentum</p>
    </section>

    <section class="sign-off">
      <div>Sincerely,</div>
      <div class="signature-area" role="img" aria-label="Handwritten signature of Daniel Whitford"></div>
      <div class="signer-name">Daniel Whitford</div>
      <div>President / CEO</div>
    </section>

    <svg class="footer-band" viewBox="0 0 610 12" preserveAspectRatio="none">
      <polygon points="0,0 348,0 340,12 0,12" fill="var(--brand-orange)"/>
      <polygon points="354,0 610,0 610,12 346,12" fill="var(--brand-grey)"/>
    </svg>
  </main>
</body>
</html>
```